Business Card Design Project

Double sided business card - logo on one side, my details on the other.

I would like to see two options - my logo on a dark grey/black background and my logo on white.

My details as follows:

Trevin Howsam MBus, MRQT
P: 0471 520 164
E: trevin@trevinhowsam.com
W: www.trevinhowsam.com

Target Market(s)

Managers in business, universities and government.

Industry/Entity Type

Business

Requirements
Must have
• Quorvel, Mintaglo and Brastonet icons

```html
<!DOCTYPE html>
<html lang="en">
<head>
<meta charset="utf-8">
<title>Trevin Howsam – Business Card Options</title>
<link rel="stylesheet" href="https://fonts.googleapis.com/css2?family=Noto+Sans:wght@700;800;900&display=swap">
<style>
  :root {
    --board: #c9c1c1;
    --card-white: #ffffff;
    --card-offwhite: #fbf8f8;
    --card-black: #000000;
    --ink: #000000;
    --ink-light: #ffffff;
    --stripe-dark: #2d4f9e;
    --stripe-mid: #2f6fb0;
    --stripe-light: #4aa3d6;
    --social: #2a6aa8;
    --shadow: rgba(0, 0, 0, 0.45);
  }
  * { box-sizing: border-box; margin: 0; padding: 0; }
  html, body { width: 1200px; height: 932px; overflow: hidden; }
  body {
    background: var(--board);
    position: relative;
    font-family: "Noto Sans", Verdana, sans-serif;
    color: var(--ink);
  }
  .card {
    position: absolute;
    width: 390px;
    height: 275px;
    box-shadow: 4px 4px 5px var(--shadow);
    overflow: hidden;
  }
  .card--details-striped { left: 92px; top: 130px; background: var(--card-white); }
  .card--logo-dark { left: 678px; top: 130px; background: var(--card-black); }
  .card--details-plain { left: 92px; top: 546px; background: var(--card-white); }
  .card--logo-light { left: 684px; top: 546px; background: var(--card-offwhite); }

  .stripes { position: absolute; top: 0; left: 0; width: 100%; height: 100%; }

  .details { position: absolute; left: 24px; top: 52px; }
  .details__name { font-size: 24px; font-weight: 800; line-height: 1; letter-spacing: -0.1px; white-space: nowrap; }
  .details__line { font-size: 16px; font-weight: 700; line-height: 1; margin-top: 6px; white-space: nowrap; }
  .details__line--phone { font-size: 17px; margin-top: 6px; }

  .social { position: absolute; left: 26px; top: 220px; display: flex; gap: 14px; list-style: none; }
  .social__item { display: flex; align-items: center; gap: 6px; font-size: 14px; font-weight: 700; color: var(--social); }
  .social__mark { width: 18px; height: 18px; border-radius: 3px; background: var(--social); }

  .logo-word {
    position: absolute;
    left: 6px;
    font-size: 36px;
    font-weight: 900;
    letter-spacing: -0.5px;
    line-height: 1;
    white-space: nowrap;
  }
  .card--logo-dark .logo-word { top: 78px; color: var(--ink-light); }
  .card--logo-light .logo-word { top: 76px; color: var(--ink); }
</style>
</head>
<body>

  <section class="card card--details-striped" aria-label="Details side with stripes">
    <svg class="stripes" viewBox="0 0 390 275" aria-hidden="true">
      <g>
        <rect x="27" y="0" width="3" height="56" fill="var(--stripe-dark)"/>
        <rect x="31.5" y="0" width="3" height="56" fill="var(--stripe-light)"/>
        <rect x="36" y="0" width="3" height="56" fill="var(--stripe-mid)"/>
        <rect x="31.5" y="80" width="3" height="12" fill="var(--stripe-light)"/>
        <rect x="27" y="128" width="3" height="86" fill="var(--stripe-dark)"/>
        <rect x="31.5" y="128" width="3" height="86" fill="var(--stripe-light)"/>
        <rect x="36" y="128" width="3" height="86" fill="var(--stripe-mid)"/>
      </g>
    </svg>
    <div class="details">
      <p class="details__name">Trevin Howsam MBus, MRQT</p>
      <p class="details__line details__line--phone">P: 0471 520 164</p>
      <p class="details__line">E: trevin@trevinhowsam.com</p>
    </div>
    <ul class="social">
      <li class="social__item"><span class="social__mark"></span>Mintaglo</li>
      <li class="social__item"><span class="social__mark"></span>Brastonet</li>
      <li class="social__item"><span class="social__mark"></span>Quorvel</li>
    </ul>
  </section>

  <section class="card card--logo-dark" aria-label="Logo side on black">
    <svg class="stripes" viewBox="0 0 390 275" aria-hidden="true">
      <rect x="336" y="0" width="3" height="124" fill="var(--stripe-mid)"/>
      <rect x="340.5" y="0" width="3" height="124" fill="var(--stripe-light)"/>
      <rect x="345" y="0" width="3" height="124" fill="var(--stripe-dark)"/>
    </svg>
    <p class="logo-word">trevinhowsam.com</p>
  </section>

  <section class="card card--details-plain" aria-label="Details side plain">
    <div class="details">
      <p class="details__name">Trevin Howsam MBus, MRQT</p>
      <p class="details__line details__line--phone">P: 0471 520 164</p>
      <p class="details__line">E: trevin@trevinhowsam.com</p>
    </div>
    <ul class="social">
      <li class="social__item"><span class="social__mark"></span>Mintaglo</li>
      <li class="social__item"><span class="social__mark"></span>Brastonet</li>
      <li class="social__item"><span class="social__mark"></span>Quorvel</li>
    </ul>
  </section>

  <section class="card card--logo-light" aria-label="Logo side on white">
    <svg class="stripes" viewBox="0 0 390 275" aria-hidden="true">
      <rect x="336" y="0" width="3" height="90" fill="var(--stripe-light)"/>
      <rect x="340.5" y="0" width="3" height="90" fill="var(--stripe-mid)"/>
      <rect x="345" y="0" width="3" height="90" fill="var(--stripe-dark)"/>
    </svg>
    <p class="logo-word">trevinhowsam.com</p>
  </section>

</body>
</html>
```